Yoga and Wellness Center

New business- have the logo already, but wanted my cards to be more colorful.

Please find my attached logo. I am only waiting on confirmation of my
telephone number in order to have all the information right. This is for a
new yoga and wellness center in TN for a conservative audience, but I would
like a colorful business card.

Industry/Entity Type

Conservative

```html
<!DOCTYPE html>
<html lang="en">
<head>
<meta charset="utf-8">
<title>Cedar Hollow Yoga – Business Card</title>
<link rel="stylesheet" href="https://fonts.googleapis.com/css2?family=Lato:wght@400;700;900&display=swap">
<style>
  :root {
    --backdrop: #2e2e2e;
    --card-white: #ffffff;
    --wave-grey: #b9b9b9;
    --brand-navy: #24287a;
    --brand-orange: #e3611d;
    --brand-orange-deep: #cf5214;
    --ink-dark: #1e1e2a;
    --text-light: #ffffff;
  }
  * { margin: 0; padding: 0; box-sizing: border-box; }
  html, body {
    width: 1200px;
    height: 1116px;
    overflow: hidden;
    background: var(--backdrop);
    font-family: "Lato", Arial, sans-serif;
  }
  .canvas {
    position: relative;
    width: 1200px;
    height: 1116px;
  }
  .business-card {
    position: absolute;
    left: 100px;
    top: 272px;
    width: 1000px;
    height: 572px;
    background: var(--card-white);
    overflow: hidden;
    box-shadow: 0 18px 40px rgba(0, 0, 0, 0.55);
  }
  .card-waves {
    position: absolute;
    inset: 0;
    width: 100%;
    height: 100%;
  }
  .brand-name {
    position: absolute;
    left: 480px;
    top: 120px;
    display: flex;
    align-items: center;
    gap: 14px;
    color: var(--brand-navy);
    font-weight: 900;
    font-size: 34px;
    letter-spacing: 3px;
    text-transform: uppercase;
  }
  .brand-dot {
    width: 46px;
    height: 46px;
    border-radius: 50%;
    background: var(--brand-orange);
    flex: none;
  }
  .owner {
    position: absolute;
    right: 70px;
    top: 360px;
    text-align: right;
  }
  .owner-name {
    color: var(--brand-navy);
    font-weight: 900;
    font-size: 34px;
  }
  .owner-title {
    color: var(--ink-dark);
    font-weight: 700;
    font-size: 17px;
    letter-spacing: 0.5px;
    margin-top: 4px;
  }
  .contact-list {
    position: absolute;
    left: 70px;
    top: 395px;
    list-style: none;
    color: var(--text-light);
    font-size: 22px;
    line-height: 1.3;
  }
  .contact-item {
    display: flex;
    align-items: flex-start;
    gap: 14px;
    margin-bottom: 10px;
  }
  .contact-icon {
    width: 22px;
    height: 22px;
    margin-top: 3px;
    flex: none;
    fill: var(--brand-navy);
  }
</style>
</head>
<body>
<main class="canvas">
  <section class="business-card">
    <svg class="card-waves" viewBox="0 0 1000 572" preserveAspectRatio="none" aria-hidden="true">
      <defs>
        <linearGradient id="orangeFill" x1="0" y1="0" x2="1" y2="1">
          <stop offset="0" stop-color="var(--brand-orange)"/>
          <stop offset="1" stop-color="var(--brand-orange-deep)"/>
        </linearGradient>
      </defs>
      <path class="wave-grey" d="M300,330 C600,300 820,200 1000,100 L1000,160 C760,270 560,330 300,330 Z" fill="var(--wave-grey)"/>
      <path class="wave-navy" d="M0,290 C280,350 600,320 1000,148 L1000,572 L0,572 Z" fill="var(--brand-navy)"/>
      <path class="wave-orange" d="M0,312 C290,370 610,338 1000,168 L1000,572 L0,572 Z" fill="url(#orangeFill)"/>
    </svg>

    <div class="brand-name">
      <span class="brand-dot"></span>
      <span>Cedar Hollow Yoga</span>
    </div>

    <div class="owner">
      <p class="owner-name">Daniel Harper</p>
      <p class="owner-title">OWNER / FOUNDER</p>
    </div>

    <ul class="contact-list">
      <li class="contact-item">
        <svg class="contact-icon" viewBox="0 0 24 24" aria-hidden="true"><path d="M6.6 10.8a15.1 15.1 0 0 0 6.6 6.6l2.2-2.2a1 1 0 0 1 1-.25 11.4 11.4 0 0 0 3.6.57 1 1 0 0 1 1 1V20a1 1 0 0 1-1 1A17 17 0 0 1 3 4a1 1 0 0 1 1-1h3.5a1 1 0 0 1 1 1c0 1.25.2 2.45.57 3.57a1 1 0 0 1-.25 1z"/></svg>
        <span>(520) 555-0148</span>
      </li>
      <li class="contact-item">
        <svg class="contact-icon" viewBox="0 0 24 24" aria-hidden="true"><path d="M2 5h20v14H2z M2 5l10 8 10-8" fill="var(--brand-navy)"/><path d="M3 6l9 7 9-7" fill="none" stroke="#e3611d" stroke-width="1.5"/></svg>
        <span>daniel@cedarhollow.com</span>
      </li>
      <li class="contact-item">
        <svg class="contact-icon" viewBox="0 0 24 24" aria-hidden="true"><path d="M12 2a7 7 0 0 0-7 7c0 5.2 7 13 7 13s7-7.8 7-13a7 7 0 0 0-7-7zm0 9.5A2.5 2.5 0 1 1 12 6.5a2.5 2.5 0 0 1 0 5z"/></svg>
        <span>2150 E. Linden Ave., Ste. 210<br>Marlow, Arizona 85600</span>
      </li>
    </ul>
  </section>
</main>
</body>
</html>
```